HPW Flyer

To design a 2 sided flyer that will fit in a DL size envelope for Pipeline Renewal Works. We replace peoples old drains with brand new drains so that they can stop spending money on cleaning the drains. Also, lots of houses have cracked drains but they think that it will be too expensive to fix. The logo and content are attached. The website is available to view at www.pipelinerenewalworks.com.au.

Target Market(s)

Owners of older homes with earthenware drains who need new pvc drains

Contact Information for Business Card

Information to go on card:
Toby Marsh
0427385160
toby@hpwexample.com.au
www.pipelinerenewalworks.com.au
PGE 918273

```html
<!DOCTYPE html>
<html lang="en">
<head>
<meta charset="utf-8">
<title>HPW Flyer</title>
<link href="https://fonts.googleapis.com/css2?family=Montserrat:wght@700;800&family=Arimo:wght@400;700&display=swap" rel="stylesheet">
<style>
:root{
  --bg:#2b2b2e;
  --navy:#0f4f9a;
  --navy-deep:#0a3c7a;
  --sky:#1fa9e6;
  --sky-light:#34b8ef;
  --orange:#f0932b;
  --button:#0d4a8f;
  --white:#ffffff;
  --ink:#1a1a1a;
  --brand:#1577c9;
}
*{margin:0;padding:0;box-sizing:border-box}
html,body{width:1200px;height:2268px;overflow:hidden;background:var(--bg)}
.flyer{position:absolute;left:20px;top:10px;width:1160px;height:2248px;background:var(--white);overflow:hidden}
.header{position:absolute;left:0;top:0;width:100%;height:905px;background:linear-gradient(180deg,#1c6cc0 0%,var(--navy) 55%,var(--navy-deep) 100%)}
.headline{position:absolute;left:150px;top:60px;width:960px;font-family:"Montserrat",sans-serif;font-weight:800;font-size:68px;line-height:76px;color:var(--white);text-shadow:0 4px 8px rgba(0,0,0,.35)}
.service{position:absolute;left:0;top:905px;width:100%;height:475px;background:linear-gradient(180deg,var(--sky-light),var(--sky))}
.photo{position:absolute;left:125px;top:640px;width:900px;height:560px;border:12px solid var(--white);transform:rotate(-6deg);box-shadow:0 10px 24px rgba(0,0,0,.35);background:linear-gradient(100deg,#5f7890 0%,#8aa0b4 45%,#d98a2c 70%,#4a5662 100%)}
.photo-caption{position:absolute;left:40px;bottom:60px;font-family:"Montserrat",sans-serif;font-weight:800;font-size:44px;line-height:52px;color:var(--white);text-shadow:0 3px 6px rgba(0,0,0,.5)}
.intro{position:absolute;left:150px;top:1255px;width:860px;text-align:center;font-family:"Arimo",sans-serif;font-size:28px;line-height:38px;color:var(--white)}
.cta-band{position:absolute;left:0;top:1380px;width:100%;height:430px;background:var(--orange)}
.call-button{position:absolute;left:165px;top:120px;width:675px;height:235px;border-radius:16px;background:linear-gradient(180deg,#1660ad,var(--button));box-shadow:0 8px 16px rgba(0,0,0,.3);display:flex;align-items:center}
.call-icon{margin-left:45px;width:96px;height:96px;flex:none}
.call-text{margin-left:40px;color:var(--white);font-family:"Arimo",sans-serif}
.call-lead{font-size:32px;line-height:44px}
.call-lead b{font-weight:700}
.call-number{font-family:"Montserrat",sans-serif;font-weight:700;font-size:70px;line-height:84px}
.contact{position:absolute;left:0;top:1820px;width:100%;text-align:center;font-family:"Arimo",sans-serif;font-size:34px;line-height:68px;color:var(--ink)}
.brand{position:absolute;left:0;top:2060px;width:100%;display:flex;justify-content:center;align-items:center;gap:22px}
.brand-mark{width:70px;height:70px;background:var(--brand)}
.brand-name{font-family:"Montserrat",sans-serif;font-weight:800;font-size:50px;color:var(--brand)}
</style>
</head>
<body>
<main class="flyer">
  <section class="header">
    <h1 class="headline">Call today to find out how to receive a $150 discount. All work completed by licensed plumbers. Guaranteed workmanship</h1>
  </section>
  <section class="service">
    <p class="intro">We clean your drain then put a CCTV camera down the drain to assess where the issues are and how badly damaged the drain is.</p>
  </section>
  <div class="photo" role="img" aria-label="Plumber holding a thermal inspection camera over a drain">
    <p class="photo-caption">We also<br>offer a drain<br>cleaning service</p>
  </div>
  <section class="cta-band">
    <div class="call-button">
      <svg class="call-icon" viewBox="0 0 96 96" aria-hidden="true">
        <circle cx="48" cy="48" r="46" fill="#0a3a72"/>
        <path d="M34 24c3 0 5 7 6 10 1 3-4 5-4 7 1 6 9 14 15 15 2 0 4-5 7-4 3 1 10 3 10 6 0 4-5 10-10 10-16-1-33-18-34-34 0-5 6-10 10-10z" fill="#fff"/>
      </svg>
      <div class="call-text">
        <p class="call-lead">Can't Wait? <b>Call Us Today</b></p>
        <p class="call-number">0427 385 160</p>
      </div>
    </div>
  </section>
  <section class="contact">
    <p>or email toby@hpwexample.com.au</p>
    <p>or visit</p>
    <p>www.pipelinerenewalworks.com.au</p>
  </section>
  <div class="brand">
    <span class="brand-mark"></span>
    <span class="brand-name">Pipeline Renewal Works</span>
  </div>
</main>
</body>
</html>
```